I need a website built for my modeling agency company.

On our website, a user can create a profile and we will submit it to thousands of modeling agents throughout the country.

In many cases, they will receive multiple offers from modeling agencies which allows them to pick and choose the contract that is best for them to launch their modeling career.

Some tag lines to consider using:

"Submit your profile to hundreds of modeling agents instantly!"

"Get found and become a star!"

We are: The Runway Guild.

Our Slogan: The World''s Largest Network of Fashion Models and Agents

What We Do: We are an agency with one of the largest networks of fashion professionals that are looking for new modeling talent. We host professional profiles for aspiring models, professional fashion models seeking work, modeling talent seekers, and top modeling agencies. We connect aspiring models with the top modeling agencies in the United States and abroad.

By submitting your FREE profile, you will be instantly introduced to the industry’s leading modeling agents. Within a few days, you could receive multiple, competing offers from modeling agencies that all want to launch your modeling career. Receiving multiple signing offers puts you in control of deciding which contract best suites you!

Reason: I've seen some good designs, but none that are 100% perfect. These are the ones that I like best so far (to give you some ideas): http://files.pixelvantor.com/img/501132/770214/770214_3391045_501132_image.jpg http://files.pixelvantor.com/img/501132/768531/768531_3397712_501132_image.jpg http://files.pixelvantor.com/img/501132/52817/52817_3394420_501132_image.jpg http://files.pixelvantor.com/img/501132/52817/52817_3389163_501132_image.jpg http://files.pixelvantor.com/img/501132/773906/773906_3390287_501132_image.jpg

Target Market(s)

Aspiring models (mostly female, but some male)

Industry/Entity Type

Modeling Agency

Colors

Designer to choose colors to be used in the design.

Requirements
Nice to have
• Somewhere in the top half of the page, I would like there to be a small form for the visitor to fill out. This form will look as follows:

Title: Instantly contact hundreds of modeling agents who are looking for new talent and could make you a star!
Fields: First Name*, Last Name*, Age, Zip Code, Email Address*, Daytime Phone, Evening Phone, Comments.

Then, there will be a "submit" button to proceed to next step of form. Just below the "submit" button, should be the following verbiage: "You will have the opportunity to upload photo(s) and provide other pertinent information in next step."

```html
<!DOCTYPE html>
<html lang="en">
<head>
<meta charset="utf-8">
<title>The Runway Guild</title>
<link href="https://fonts.googleapis.com/css2?family=Roboto:wght@300;400;700&display=swap" rel="stylesheet">
<style>
:root{
  --pink:#d4075f;
  --ink:#1a1a1a;
  --text:#333333;
  --muted:#555555;
  --rule:#dddddd;
  --white:#ffffff;
  --black:#000000;
}
*{margin:0;padding:0;box-sizing:border-box}
html,body{width:864px;height:1200px;overflow:hidden;background:var(--white)}
body{position:relative;font-family:"Roboto",Arial,sans-serif;color:var(--text)}
.abs{position:absolute}

/* header */
.site-header{position:absolute;left:0;top:0;width:864px;height:62px;background:var(--white)}
.main-nav{position:absolute;left:146px;top:23px;display:flex;align-items:center;gap:11px;font-size:9.5px;font-weight:300;color:var(--ink);letter-spacing:.1px}
.brand{position:absolute;left:0;width:864px;top:16px;text-align:center}
.brand-name{font-size:17px;font-weight:400;color:var(--ink);letter-spacing:1.5px;text-transform:uppercase;line-height:1}
.brand-tag{font-size:5.6px;font-weight:400;color:var(--ink);margin-top:3px}
.btn{position:absolute;top:22px;height:18px;width:54px;font-size:8px;color:var(--white);display:flex;align-items:center;justify-content:center}
.btn-login{left:606px;background:var(--pink)}
.btn-register{left:664px;background:var(--black)}

/* hero */
.hero{position:absolute;left:0;top:62px;width:864px;height:299px;overflow:hidden;
  background:linear-gradient(100deg,#7b3b22 0%,#9c5433 25%,#b57a52 45%,#a86a44 60%,#8d5a3c 80%,#6e4330 100%)}
.hero-shade{position:absolute;inset:0;background:radial-gradient(ellipse at 55% 40%,rgba(255,220,180,.18),rgba(0,0,0,.25) 80%)}
.hero-title{position:absolute;left:0;width:864px;top:178px;text-align:center;font-size:26px;font-weight:300;line-height:30px;color:var(--white)}
.hero-dots{position:absolute;left:400px;top:282px;display:flex;gap:5px}
.hero-dots span{width:7px;height:7px;border-radius:50%;background:#222}
.hero-dots span.active{background:var(--pink)}

/* sections */
.section-title{position:absolute;display:flex;align-items:center;gap:9px;font-size:21.5px;font-weight:300;color:var(--ink)}
.intro{position:absolute;left:140px;width:584px;top:422px;text-align:center;font-size:13.6px;font-weight:300;line-height:16.5px;color:var(--ink)}
.divider{position:absolute;left:146px;top:488px;width:572px;height:1px;background:var(--rule)}
.step{position:absolute;top:552px;width:190px;text-align:center}
.step-num{font-size:33px;font-weight:300;color:var(--pink);line-height:40px}
.step-text{margin-top:14px;font-size:8.6px;font-weight:300;line-height:14px;color:var(--ink)}
.step-text b{font-weight:700}

/* models */
.model{position:absolute;top:752px;width:168px;height:168px;border-radius:50%;background:var(--white);box-shadow:0 3px 14px rgba(0,0,0,.18)}
.model-photo{position:absolute;left:12px;top:12px;width:144px;height:144px;border-radius:50%;overflow:hidden}
.model-overlay{position:absolute;left:0;top:92px;width:144px;height:52px;background:var(--pink);color:var(--white);font-size:8.6px;font-weight:300;text-align:center;padding-top:10px}

/* footer */
.contact-band{position:absolute;left:0;top:1019px;width:864px;height:61px;background:var(--pink)}
.contact-text{position:absolute;left:149px;top:25px;font-size:8.6px;font-weight:300;color:var(--white)}
.contact-text b{font-weight:700}
.social{position:absolute;top:26px;width:11px;height:11px;border-radius:50%;background:var(--white)}
.site-footer{position:absolute;left:0;top:1080px;width:864px;height:120px;background:var(--black);color:var(--white)}
.footer-nav{position:absolute;left:149px;top:12px;display:flex;gap:6px;font-size:8.6px;font-weight:300}
.copyright{position:absolute;right:148px;top:12px;font-size:8.6px;font-weight:300}
.footer-mark{position:absolute;left:0;width:864px;top:44px;text-align:center;font-size:38px;font-weight:300;letter-spacing:3px;text-transform:uppercase;color:#2c2c2c}
</style>
</head>
<body>

<header class="site-header">
  <nav class="main-nav">
    <svg width="12" height="11" viewBox="0 0 12 11"><path d="M6 0 L12 5.5 H10.3 V11 H7.3 V7.5 H4.7 V11 H1.7 V5.5 H0 Z" fill="var(--pink)"/></svg>
    <span>ABOUT US</span><span>WHY US?</span><span>CONTACT US</span>
  </nav>
  <div class="brand">
    <div class="brand-name">The Runway Guild</div>
    <div class="brand-tag">The World's Largest Network of Fashion Models and Agents</div>
  </div>
  <a class="btn btn-login">Login</a>
  <a class="btn btn-register">Register</a>
</header>

<section class="hero">
  <div class="hero-shade" role="img" aria-label="Photo of a young woman in a denim vest and floral dress standing against a brick wall"></div>
  <svg class="abs" style="left:16px;top:125px" width="34" height="62" viewBox="0 0 34 62"><path d="M32 1 L2 31 L32 61" fill="none" stroke="#fff" stroke-width="1.2"/></svg>
  <svg class="abs" style="left:814px;top:125px" width="34" height="62" viewBox="0 0 34 62"><path d="M2 1 L32 31 L2 61" fill="none" stroke="#fff" stroke-width="1.2"/></svg>
  <h1 class="hero-title">Submit your profile to hundreds of modeling<br>agents instantly!</h1>
  <div class="hero-dots"><span class="active"></span><span></span><span></span><span></span><span></span></div>
</section>
<svg class="abs" style="left:0;top:62px" width="864" height="30" viewBox="0 0 864 30"><path d="M382 0 C410 0 426 6 432 28 C438 6 454 0 482 0 Z" fill="var(--white)"/></svg>

<h2 class="section-title" style="left:355px;top:384px">
  <svg width="16" height="15" viewBox="0 0 16 15"><path d="M1 0 H15 A1 1 0 0 1 16 1 V10 A1 1 0 0 1 15 11 H7 L3 15 V11 H1 A1 1 0 0 1 0 10 V1 A1 1 0 0 1 1 0 Z" fill="var(--pink)"/><circle cx="4.5" cy="5.5" r="1.1" fill="#fff"/><circle cx="8" cy="5.5" r="1.1" fill="#fff"/><circle cx="11.5" cy="5.5" r="1.1" fill="#fff"/></svg>
  What We Do ?
</h2>
<p class="intro">We are an association that hosts profiles for aspiring models, professional fashion models seeking work, modeling agencies, and modeling talent agents. We connect aspiring models with the top modeling agencies in the United States and abroad.</p>
<div class="divider"></div>

<h2 class="section-title" style="left:147px;top:513px">
  <svg width="21" height="16" viewBox="0 0 21 16"><rect x="2.5" y="1" width="16" height="11" rx="1" fill="none" stroke="var(--pink)" stroke-width="2"/><path d="M0 14 H21 V16 H0 Z" fill="var(--pink)"/><path d="M7 6.5 L9.5 9 L14 4" fill="none" stroke="var(--pink)" stroke-width="1.8"/></svg>
  What You Have To Do ?
</h2>

<div class="step" style="left:141px">
  <div class="step-num">1.</div>
  <p class="step-text">Make an account on our website and complete your model profile. Upload your best photos and <b>get found and become a star!</b></p>
</div>
<div class="step" style="left:341px">
  <div class="step-num">2.</div>
  <p class="step-text"><b>THE RUNWAY GUILD,</b> The World's Largest Network of Fashion Models and Agents will promote your profile to thousands model agencies.</p>
</div>
<div class="step" style="left:534px">
  <div class="step-num">3.</div>
  <p class="step-text">Login daily into your model account and choose the contract you think that suits you most. Get ready to be a star.</p>
</div>

<h2 class="section-title" style="left:148px;top:693px">
  <svg width="15" height="16" viewBox="0 0 15 16"><circle cx="7.5" cy="3" r="2.6" fill="var(--pink)"/><circle cx="2.6" cy="5" r="2" fill="var(--pink)"/><circle cx="12.4" cy="5" r="2" fill="var(--pink)"/><path d="M4.5 7 H10.5 V13 H9 V16 H6 V13 H4.5 Z M0 8 H4 V13 H0 Z M11 8 H15 V13 H11 Z" fill="var(--pink)"/></svg>
  New Models On Our Website
</h2>

<div class="model" style="left:145px">
  <div class="model-photo" role="img" aria-label="Portrait photo of a smiling model with long brown hair and a fur scarf" style="background:radial-gradient(circle at 50% 45%,#a37a66,#5e3c33 75%)"></div>
</div>
<div class="model" style="left:346px">
  <div class="model-photo" role="img" aria-label="Portrait photo of a model wearing a patterned headband" style="background:radial-gradient(circle at 50% 40%,#c7b1a4,#6f6a6c 75%)">
    <div class="model-overlay">
      <svg width="11" height="12" viewBox="0 0 11 12"><circle cx="5.5" cy="3" r="3" fill="#fff"/><path d="M0 12 C0 7.5 2.5 6.5 5.5 6.5 C8.5 6.5 11 7.5 11 12 Z" fill="#fff"/></svg>
      <div style="margin-top:3px">View model's profile</div>
    </div>
  </div>
</div>
<div class="model" style="left:550px">
  <div class="model-photo" role="img" aria-label="Photo of a model holding a green hat by a lake in the woods" style="background:radial-gradient(circle at 50% 45%,#9a8c5e,#3f4a2a 75%)"></div>
</div>

<svg class="abs" style="left:0;top:976px" width="864" height="45" viewBox="0 0 864 45"><path d="M370 44 C410 44 426 28 432 2 C438 28 454 44 494 44 Z" fill="var(--pink)"/></svg>
<section class="contact-band">
  <p class="contact-text">Need more informations, please feel free to <b>contact us</b></p>
  <span class="social" style="left:681px" aria-label="Social profile"></span>
  <span class="social" style="left:704px" aria-label="Social profile"></span>
</section>

<footer class="site-footer">
  <nav class="footer-nav"><span>Home</span><span>About Us</span><span>Why Us</span><span>Contact Us</span></nav>
  <p class="copyright">All rights reserved 2013</p>
  <div class="footer-mark">The Runway Guild</div>
</footer>

</body>
</html>
```